Wanderlark Gin - Bottle Label for a craft Gin about to be launched on the world from New Zealand

We are a start up craft distillery in New Zealand. We have developed a wonderful Gin using our own grain spirit and both traditional and New Zealand native botanicals (Manuka to be specific), chosen our bottle and the name "Wanderlark" and done a bit of amateur label design and now we are looking for someone to make it great.

Feel free to change up our amateur concept but give us something that will pop from the back bar and scream authenticity, craft and individuality.

The attached files give you the specifications of the bottle, our current concept for a Wanderlark label and an earlier concept drawing that gives an idea of where we are thinking the two labels should go on the front of the bottle.

Thanks, we look forward to your ideas!!

Target Market(s)

High end and craft Gin drinkers. Hipsters and cocktail barflys and their bar tenders and bar owners

Requirements
Must have
• Attractive individuality
Nice to have
• Coolness
Should not have
• Uncoolness

```html
<!DOCTYPE html>
<html lang="en">
<head>
<meta charset="utf-8">
<title>Wanderlark Gin – Bottle Label</title>
<link rel="stylesheet" href="https://fonts.googleapis.com/css2?family=Staatliches&family=Playball&display=swap">
<style>
  :root {
    --paper: #ffffff;
    --ink: #111111;
    --navy: #1c1f4a;
    --leaf: #3aa53a;
  }
  html, body {
    margin: 0;
    padding: 0;
    width: 1200px;
    height: 2632px;
    overflow: hidden;
    background: var(--paper);
  }
  .canvas {
    position: relative;
    width: 1200px;
    height: 2632px;
  }
  .band {
    position: absolute;
    left: 50%;
    transform: translateX(-50%);
  }
  .band--black { background: var(--ink); }
  .band--green { background: var(--leaf); }

  .neck-label .recipe {
    position: absolute;
    top: 495px;
    left: 0;
    width: 1200px;
    text-align: center;
    font-family: "Playball", cursive;
    font-size: 40px;
    color: var(--navy);
    margin: 0;
  }
  .neck-band-green { top: 578px; width: 316px; height: 7px; }
  .neck-band-black { top: 592px; width: 316px; height: 9px; }

  .main-band-top-black { top: 1239px; width: 652px; height: 14px; }
  .main-band-top-green { top: 1270px; width: 652px; height: 7px; }
  .main-band-bottom-green { top: 1662px; width: 652px; height: 7px; }
  .main-band-bottom-black { top: 1683px; width: 652px; height: 14px; }

  .wordmark {
    position: absolute;
    top: 1340px;
    left: 0;
    width: 1200px;
    text-align: center;
    font-family: "Staatliches", sans-serif;
    font-size: 132px;
    line-height: 1;
    letter-spacing: 2px;
    color: var(--ink);
    margin: 0;
  }
  .tagline {
    position: absolute;
    top: 1498px;
    left: 0;
    width: 1200px;
    text-align: center;
    font-family: "Playball", cursive;
    font-size: 46px;
    color: var(--navy);
    margin: 0;
  }
  .dots {
    position: absolute;
    top: 1595px;
    left: 557px;
  }
  .description {
    position: absolute;
    top: 1750px;
    left: 0;
    width: 1200px;
    text-align: center;
    font-family: "Playball", cursive;
    font-size: 29px;
    line-height: 40px;
    color: var(--ink);
    margin: 0;
  }
</style>
</head>
<body>
<main class="canvas">
  <section class="neck-label">
    <p class="recipe">Recipe #3</p>
    <div class="band band--green neck-band-green"></div>
    <div class="band band--black neck-band-black"></div>
  </section>

  <section class="main-label">
    <div class="band band--black main-band-top-black"></div>
    <div class="band band--green main-band-top-green"></div>
    <h1 class="wordmark">WANDERLARK</h1>
    <p class="tagline">New Zealand small batch Gin</p>
    <svg class="dots" width="86" height="32" viewBox="0 0 86 32" aria-hidden="true">
      <circle cx="16" cy="16" r="15" fill="var(--ink)"/>
      <circle cx="64" cy="16" r="15" fill="var(--ink)"/>
    </svg>
    <div class="band band--green main-band-bottom-green"></div>
    <div class="band band--black main-band-bottom-black"></div>
  </section>

  <p class="description">A classically inspired Gin<br>with developed citrus notes from<br>the Manuka berries from<br>Marcus's mates. Best with an<br>equal mix of some fancy tonic.</p>
</main>
</body>
</html>
```